Advertising Agencies

I am a consumer product contract manufacturing and packaging consultant. I service the following industries: food, nutritional supplements, hair care, skin care, cosmetics and electronics. I serve as a 3rd party supply chain management solution so that my customers can focus on selling their product and growing their business vs. dealing with the actual manufacturing & packaging of their product. Advertising agencies are often contacted in the early stages of product design. During this early stage is an ideal time for us to take a look at the product, manufacturing & packaging and provide feedback on feasibility, cost, lead times, etc. We need a postcard that encourages the production manager at the advertising agency to include us (at no cost) at the 'round table' early in the product design stages.

Per the attached clip art: I'm envisioning something like this, eye catching, that depicts the various people at the board room meeting: The consumer product company owner, the ad firm designer, the ad firm PR/marketing person and myself the manufacturing & packaging consultant. Perhaps centered on the table will be a 2oz all natural shot drink with a shrink sleeve on it & inside its display box.

Websites:
Harborlinestudioeast.com
PrimeDose.com
7KVRT.site.mobi - Tablet or smartphone mobile site
Some copy that could be used on the card: http://www.wrapfolio-example.com/contract-packaging/strategy/why-contract-packagers-need-be-involved-early-product-development-cycle

```html
<!DOCTYPE html>
<html lang="en">
<head>
<meta charset="utf-8">
<title>Early Involvement Postcard</title>
<link href="https://fonts.googleapis.com/css2?family=Oswald:wght@300;400;600;700&family=Arimo:wght@400;700&display=swap" rel="stylesheet">
<style>
  :root {
    --brand-blue: #1596c6;
    --brand-blue-dark: #0f86b4;
    --sky-blue: #a9dcf5;
    --ink-gray: #444448;
    --panel-dark: #2c2c2e;
    --panel-mid: #58585b;
    --paper: #ffffff;
  }
  * { box-sizing: border-box; margin: 0; padding: 0; }
  html, body { width: 1200px; height: 900px; overflow: hidden; background: #e9e9e9; }
  .postcard { position: relative; width: 1200px; height: 900px; background: var(--paper); overflow: hidden; font-family: "Arimo", Arial, sans-serif; }
  .postcard__shapes { position: absolute; inset: 0; }
  .hero-illustration {
    position: absolute; left: 52px; top: 30px; width: 500px; height: 480px;
    background: linear-gradient(165deg, #f3f9fc 0%, #d4ecf7 45%, #9fd3ea 80%, #6a7d88 100%);
  }
  .headline {
    position: absolute; right: 33px; top: 52px; width: 760px; text-align: right;
    font-family: "Oswald", "Arial Narrow", sans-serif; font-weight: 600;
    font-size: 31px; line-height: 40px; color: var(--brand-blue); text-transform: uppercase; letter-spacing: 0.3px;
  }
  .lead {
    position: absolute; right: 33px; top: 148px; width: 530px; text-align: right;
    font-weight: 700; font-size: 16.5px; line-height: 22px; color: var(--ink-gray);
  }
  .event-box {
    position: absolute; left: 837px; top: 346px; width: 337px; height: 360px;
    color: var(--paper); text-align: center; padding-top: 22px;
  }
  .event-box__title {
    font-family: "Oswald", "Arial Narrow", sans-serif; font-weight: 600;
    font-size: 44px; line-height: 50px; text-transform: uppercase;
  }
  .event-box__kicker { font-weight: 700; font-size: 28px; line-height: 31px; margin-top: 2px; }
  .event-box__kicker--small { font-size: 24px; line-height: 28px; }
  .event-box__text {
    font-family: "Oswald", "Arial Narrow", sans-serif; font-weight: 300;
    font-size: 14.5px; line-height: 22px; text-transform: uppercase; margin: 8px auto 0; width: 260px;
  }
  .about__title {
    position: absolute; left: 33px; top: 616px;
    font-family: "Oswald", "Arial Narrow", sans-serif; font-weight: 600;
    font-size: 46px; line-height: 56px; color: var(--sky-blue); text-transform: uppercase;
  }
  .about__text {
    position: absolute; left: 33px; top: 680px; width: 1125px;
    font-weight: 700; font-size: 16.3px; line-height: 22px; color: var(--paper);
  }
  .about__text p + p { margin-top: 6px; }
</style>
</head>
<body>
<main class="postcard">
  <div class="hero-illustration" role="img" aria-label="Illustration of a product team seated around a round boardroom table while a presenter points to a board labelled Strategy"></div>

  <svg class="postcard__shapes" viewBox="0 0 1200 900" width="1200" height="900" aria-hidden="true">
    <defs>
      <linearGradient id="panelShade" x1="0" y1="0" x2="1" y2="1">
        <stop offset="0" stop-color="#58585b"/>
        <stop offset="0.45" stop-color="#3e3e41"/>
        <stop offset="1" stop-color="#2c2c2e"/>
      </linearGradient>
    </defs>
    <polygon class="panel-dark" points="0,470 250,535 1200,282 1200,900 0,900" fill="url(#panelShade)"/>
    <polygon class="band-blue" points="0,365 250,505 900,355 900,395 250,560 0,440" fill="var(--brand-blue)"/>
    <polyline class="band-white" points="0,452 250,580 1200,335" fill="none" stroke="var(--paper)" stroke-width="14"/>
    <path class="event-box__shape" d="M837,346 L1174,346 L1174,665 Q1174,705 1134,705 L877,705 Q837,705 837,665 Z" fill="var(--brand-blue)"/>
    <polygon class="event-box__tab" points="1174,271 1174,346 1120,346" fill="var(--brand-blue-dark)"/>
    <line x1="240" y1="642" x2="506" y2="642" stroke="var(--paper)" stroke-width="3"/>
    <line x1="240" y1="657" x2="772" y2="657" stroke="var(--paper)" stroke-width="3"/>
    <polygon class="footer-white" points="0,860 895,804 1200,841 1200,900 0,900" fill="var(--paper)"/>
    <polygon class="footer-blue" points="0,874 895,818 1200,855 1200,900 0,900" fill="var(--brand-blue)"/>
  </svg>

  <h1 class="headline">Why contract packagers need to be involved early<br>in the product development cycle</h1>
  <p class="lead">The Alliance for Supply Partnerships (A4SP) recently completed an exercise in which supplier members, including contract packaging and logistics service providers, characterized what they see as best practices of leading customers.</p>

  <section class="event-box">
    <h2 class="event-box__title">Save us a seat<br>at your table</h2>
    <p class="event-box__kicker">AT NO COST TO YOU</p>
    <p class="event-box__kicker event-box__kicker--small">EARLY INPUT</p>
    <p class="event-box__text">Invite us to the round table at the design stage and we review your product, its manufacturing and packaging for feasibility, cost and lead times before a single unit is made.</p>
  </section>

  <h2 class="about__title">About Us</h2>
  <div class="about__text">
    <p>Keystone Pack Partners is a consumer product contract manufacturing and packaging<br>consultancy serving food, supplements, hair care, skin care, cosmetics and electronics.</p>
    <p>As your 3rd party supply chain management solution, we handle the actual manufacturing and packaging so your clients can focus on selling their product and growing their business. Visit Harborlinestudioeast.com and PrimeDose.com, or reach us on a tablet or smartphone at 7KVRT.site.mobi.</p>
  </div>
</main>
</body>
</html>
```